Fun Language School in San Diego, CA - We want cool Business Card

We need a new business card design for our new logo. We are a language school in beautiful San Diego, California. Our target is students from all over the world who age from 18 to 25. They come to our school to learn English. Our school has a modern look, trending and fun place. We are the only language school who use tablets in class. We are student oriented, Students Come First is our slogan. We are re-branding ourselves with a new logo. We would like to see a designs that use our new logo and it should reflect the feel of young, fun, modern, high-tech and attractive to young people.
I've seen some business card designs with transparent look, unusual shapes, we are open to any cool ideas. Thank you very much!

In order for you to know more about our school, here are the links to our Youtube Channel and Facebook.

Youtube: https://www.vidmarlo.example/channel/ZXpolrT-48kwb2nH7c5DqLm
Facebook: https://www.friendlane.example/BVSchool

Target Market(s)

Our target is students from all over the world who age from 18 to 25. International students.

Industry/Entity Type

School

Font styles to use
Sans Serif

Requirements
Must have
• Our new logo. Name, title and address.
Should not have
• Other colors other than the ones we have in our logo. Characters are fine.

```html
<!DOCTYPE html>
<html lang="en">
<head>
<meta charset="utf-8">
<title>Bayvale School – Business Card</title>
<link rel="stylesheet" href="https://fonts.googleapis.com/css2?family=Exo+2:wght@400;500;600&display=swap">
<style>
  :root {
    --page: #e9ecef;
    --card: #ffffff;
    --sky: #5a9ec8;
    --lime: #cfdc3a;
    --ink: #2b2b2b;
    --slate: #6d6f72;
    --swoosh: #3a3a3a;
    --on-sky: #ffffff;
  }
  * { box-sizing: border-box; margin: 0; padding: 0; }
  html, body { width: 1200px; height: 900px; overflow: hidden; }
  body {
    background: var(--page);
    font-family: "Exo 2", sans-serif;
    position: relative;
  }
  .card {
    position: absolute;
    left: 250px;
    width: 700px;
    height: 400px;
    border-radius: 40px;
    background: var(--card);
    overflow: hidden;
    box-shadow: 0 6px 20px rgba(0,0,0,0.15);
  }
  .card--back { top: 40px; }
  .card--front { top: 465px; }
  .card__art { position: absolute; inset: 0; width: 100%; height: 100%; }

  .brand {
    position: absolute;
    display: flex;
    align-items: center;
    gap: 14px;
    color: var(--slate);
    font-weight: 500;
    letter-spacing: 0.5px;
    white-space: nowrap;
  }
  .brand__dot {
    border-radius: 50%;
    background: var(--sky);
    flex: none;
  }
  .card--back .brand { right: 60px; top: 70px; font-size: 40px; }
  .card--back .brand__dot { width: 54px; height: 54px; }
  .card--front .brand { right: 40px; top: 48px; font-size: 40px; }
  .card--front .brand__dot { width: 60px; height: 60px; }

  .person { position: absolute; left: 52px; top: 108px; color: var(--ink); white-space: nowrap; }
  .person__name { font-size: 25px; font-weight: 600; letter-spacing: 2px; }
  .person__title { font-size: 16px; font-weight: 500; letter-spacing: 1px; margin-top: 2px; }

  .address {
    position: absolute;
    left: 52px;
    top: 262px;
    color: var(--on-sky);
    font-size: 16px;
    line-height: 1.5;
    letter-spacing: 1px;
    white-space: nowrap;
  }
  .contacts {
    position: absolute;
    right: 40px;
    bottom: 22px;
    list-style: none;
    color: var(--on-sky);
    font-size: 16px;
    letter-spacing: 1.5px;
    text-align: right;
  }
  .contacts li {
    display: flex;
    justify-content: flex-end;
    align-items: center;
    gap: 10px;
    height: 28px;
  }
  .contacts svg { width: 16px; height: 16px; fill: var(--on-sky); flex: none; }
</style>
</head>
<body>

<section class="card card--back" aria-label="Card back">
  <svg class="card__art" viewBox="0 0 700 400" preserveAspectRatio="none" aria-hidden="true">
    <path d="M0 170 C 160 190, 420 250, 700 270 L700 400 L0 400 Z" fill="var(--sky)"/>
    <path d="M70 0 C 40 40, 90 70, 260 130 C 130 80, 90 40, 110 0 Z" fill="var(--swoosh)"/>
  </svg>
  <div class="brand"><span class="brand__dot"></span>Bayvale School</div>
</section>

<section class="card card--front" aria-label="Card front">
  <svg class="card__art" viewBox="0 0 700 400" preserveAspectRatio="none" aria-hidden="true">
    <path d="M0 215 C 150 250, 400 250, 700 232 L700 400 L0 400 Z" fill="var(--sky)"/>
    <path d="M0 162 C 100 205, 220 230, 340 238 C 220 226, 90 196, 0 144 Z" fill="var(--lime)"/>
  </svg>

  <div class="brand"><span class="brand__dot"></span>Bayvale School</div>

  <div class="person">
    <p class="person__name">MARK DELANEY</p>
    <p class="person__title">Managing Director</p>
  </div>

  <p class="address">214, 6th floor, Harbor Point<br>Road SD</p>

  <ul class="contacts">
    <li>019 552 4410
      <svg viewBox="0 0 24 24"><path d="M6.6 10.8a15.1 15.1 0 0 0 6.6 6.6l2.2-2.2c.3-.3.7-.4 1-.2 1.1.4 2.3.6 3.6.6.6 0 1 .4 1 1V20c0 .6-.4 1-1 1A17 17 0 0 1 3 4c0-.6.4-1 1-1h3.5c.6 0 1 .4 1 1 0 1.3.2 2.5.6 3.6.1.3 0 .7-.2 1z"/></svg>
    </li>
    <li>019 552 4411
      <svg viewBox="0 0 24 24"><path d="M7 1h10a2 2 0 0 1 2 2v18a2 2 0 0 1-2 2H7a2 2 0 0 1-2-2V3a2 2 0 0 1 2-2zm0 3v14h10V4zm5 15.5a1 1 0 1 0 0 2 1 1 0 0 0 0-2z"/></svg>
    </li>
    <li>019 552 4412
      <svg viewBox="0 0 24 24"><path d="M7 2h8l3 3v5h1a2 2 0 0 1 2 2v9H3v-9a2 2 0 0 1 2-2h2zm2 2v6h7V6h-2V4zm-3 9v2h2v-2zm4 0v2h2v-2zm4 0v2h2v-2zm-8 4v2h2v-2zm4 0v2h2v-2zm4 0v2h2v-2z"/></svg>
    </li>
    <li>hello@bayvale.example
      <svg viewBox="0 0 24 24"><path d="M2 5h20v14H2zm2 2v.5l8 5.5 8-5.5V7zm0 2.9V17h16V9.9l-8 5.5z"/></svg>
    </li>
  </ul>
</section>

</body>
</html>
```